juice cups take away - transparent plastic

We need a design of juice cups. 2 sizes refer to uploaded file. material is transparent so you can see juice color. The are of possible print is indicated on the draw (rectangle area on the draw). We need our logo and internet page address on the cup www.tovibrook.cn. the 3 elements from logo (3 apples,TOVIBROOK'S,颂宁棠悦 ) can be separate or together. background can be black or transparent. We need 2 versions: 1. colorful using 6 colors, red, yellow, green, blue, black, gold,
2. using max. 3 colors from the above
The colors have to strong enough to be visible on a plastic cup.
We include original materials and information pls regard it as restricted only to use in this particular project. Copy or any use to other purposes not allowed.

Reason: Dear All , we get many designs but no one of them is matching all of our requirements. After reviewing them, we suggest several developments: 1. the letter for "tovi brook's" should be 7-8 mm high and 50 mm long, green color in white overlain. The green color of the font must contrast the whit overlain (so we suggest darker green then in some projects). 2. the golden Chinese name should be 6 mm high - worth a try with white overlain to achieve contrast, 3. the coal is to create visible sign of the company name on the cup - visible and easy to recognize from distance 4. pls always provide front and backside design - some projects state only one and the same side

Target Market(s)

fresh juice bar

Industry/Entity Type

Internet

Font styles to use
Sans Serif
Decorative

Requirements
Must have
• logo or logo parts on a cup , not to many colors - color increase cost, only 6 colors max possible to produce
Nice to have
• catchy idea for the cup but easy to produce
Should not have
• no background, rst of the cup has to be transparent to recognize the juice color

```html
<!DOCTYPE html>
<html lang="en">
<head>
<meta charset="utf-8">
<title>Tovibrook's juice cup print versions</title>
<link rel="stylesheet" href="https://fonts.googleapis.com/css2?family=Montserrat:wght@500;600;700&family=Noto+Sans+SC:wght@700&display=swap">
<style>
  :root {
    --bg: #000000;
    --rim: #c9ccd0;
    --clear-top: #3a3c40;
    --juice-light: #fff3a6;
    --juice-mid: #fde35a;
    --juice-deep: #f5c816;
    --brand-green: #7cbf1e;
    --brand-green-2: #93c41d;
    --brand-gold: #c49a4a;
    --url-blue: #1a9be0;
    --ink: #111111;
    --label: #ffffff;
    --fruit-red: #ef6a3c;
    --fruit-yellow: #ffd400;
    --fruit-green: #9cc71e;
    --fruit-blue: #12aee6;
    --fruit-lime: #b4d20a;
  }
  html, body {
    margin: 0;
    padding: 0;
    width: 1200px;
    height: 1200px;
    overflow: hidden;
    background: var(--bg);
  }
  .canvas {
    display: block;
    width: 1200px;
    height: 1200px;
  }
  .brand-name {
    font-family: "Montserrat", sans-serif;
    font-weight: 600;
    font-size: 44px;
    letter-spacing: 0.5px;
  }
  .brand-name-cn {
    font-family: "Noto Sans SC", sans-serif;
    font-weight: 700;
    font-size: 52px;
    letter-spacing: 4px;
  }
  .web-address {
    font-family: "Montserrat", sans-serif;
    font-weight: 500;
    font-size: 22px;
  }
  .version-label {
    font-family: "Montserrat", sans-serif;
    font-weight: 700;
    font-size: 25px;
    fill: var(--label);
  }
  .colorful .brand-name { fill: var(--brand-green); }
  .colorful .brand-name-cn { fill: var(--brand-gold); }
  .colorful .web-address { fill: var(--url-blue); }
  .two-tone .brand-name { fill: var(--brand-green-2); }
  .two-tone .brand-name-cn { fill: var(--ink); }
  .two-tone .web-address { fill: var(--ink); }
</style>
</head>
<body>
<svg class="canvas" viewBox="0 0 1200 1200" xmlns="http://www.w3.org/2000/svg">
  <defs>
    <linearGradient id="juice" x1="0" x2="1" y1="0" y2="0">
      <stop offset="0" stop-color="var(--juice-deep)"/>
      <stop offset="0.22" stop-color="var(--juice-light)"/>
      <stop offset="0.6" stop-color="var(--juice-mid)"/>
      <stop offset="1" stop-color="var(--juice-deep)"/>
    </linearGradient>
    <linearGradient id="clear" x1="0" x2="1" y1="0" y2="0">
      <stop offset="0" stop-color="#1c1d20"/>
      <stop offset="0.5" stop-color="var(--clear-top)"/>
      <stop offset="1" stop-color="#1c1d20"/>
    </linearGradient>
    <linearGradient id="fruit-multi" x1="0" x2="1" y1="0" y2="0">
      <stop offset="0" stop-color="var(--fruit-red)"/>
      <stop offset="0.5" stop-color="var(--fruit-yellow)"/>
      <stop offset="1" stop-color="var(--fruit-green)"/>
    </linearGradient>
    <linearGradient id="fruit-sea" x1="0" x2="0" y1="0" y2="1">
      <stop offset="0" stop-color="var(--fruit-blue)" stop-opacity="0"/>
      <stop offset="1" stop-color="var(--fruit-blue)" stop-opacity="0.75"/>
    </linearGradient>
    <linearGradient id="fruit-lime" x1="0" x2="1" y1="0" y2="1">
      <stop offset="0" stop-color="#cde23a"/>
      <stop offset="1" stop-color="var(--fruit-lime)"/>
    </linearGradient>
    <g id="cup-body">
      <rect x="72" y="197" width="513" height="24" rx="10" fill="var(--rim)" opacity="0.85"/>
      <path d="M92 221 H565 L537 332 H120 Z" fill="url(#clear)"/>
      <path d="M120 332 Q327 318 537 332 L500 960 H160 Z" fill="url(#juice)"/>
      <path d="M170 960 H492 L494 1016 Q330 1036 168 1016 Z" fill="var(--juice-deep)"/>
    </g>
  </defs>

  <g class="cup colorful">
    <use href="#cup-body"/>
    <text class="brand-name" x="327" y="530" text-anchor="middle">TOVIBROOK'S</text>
    <text class="brand-name-cn" x="327" y="607" text-anchor="middle">颂宁棠悦</text>
    <g role="img" aria-label="Row of three brand fruit emblems in red, yellow, green and blue">
      <rect x="150" y="640" width="358" height="158" rx="70" fill="url(#fruit-multi)" opacity="0.85"/>
      <rect x="150" y="640" width="358" height="158" rx="70" fill="url(#fruit-sea)"/>
    </g>
    <text class="web-address" x="327" y="833" text-anchor="middle">www.tovibrook.cn</text>
    <text class="version-label" x="327" y="1102" text-anchor="middle">6 colors</text>
  </g>

  <g class="cup two-tone" transform="translate(541 0)">
    <use href="#cup-body"/>
    <text class="brand-name" x="327" y="530" text-anchor="middle">TOVIBROOK'S</text>
    <text class="brand-name-cn" x="327" y="607" text-anchor="middle">颂宁棠悦</text>
    <rect x="150" y="640" width="358" height="158" rx="70" fill="url(#fruit-lime)" role="img" aria-label="Row of three brand fruit emblems in green"/>
    <text class="web-address" x="327" y="833" text-anchor="middle">www.tovibrook.cn</text>
    <text class="version-label" x="342" y="1102" text-anchor="middle">2 colors</text>
  </g>
</svg>
</body>
</html>
```